Marvia Quenby Business Cards

We Need two Business Cards with bleeds. the only difference between the two cards is the backaround color one lilac and pink. Attached we have the cards please match up the logo's and text. Take out the orange box out.

Target Market(s)

double-sided business cards

Industry/Entity Type

Business

Logo Text

match up as best as possible

Colors
f59195
d2a4cc

Requirements
Must have
• n/a
Nice to have
• n/a
Should not have
• n/a

```html
<!DOCTYPE html>
<html lang="en">
<head>
<meta charset="utf-8">
<title>Marvia Quenby-Fenwick MD – Business Cards</title>
<link rel="stylesheet" href="https://fonts.googleapis.com/css2?family=Ubuntu:wght@400;500;700&display=swap">
<style>
  :root {
    --pink: #f19195;
    --lilac: #d2a4cc;
    --ink: #111111;
    --paper: #ffffff;
    --frame: #555555;
  }
  * { margin: 0; padding: 0; box-sizing: border-box; }
  html, body { width: 1200px; height: 1000px; overflow: hidden; background: var(--paper); }
  body { position: relative; font-family: "Ubuntu", sans-serif; color: var(--ink); }

  .card { position: absolute; }

  /* Front side */
  .front { background: var(--paper); }
  .front .name { position: absolute; font-weight: 700; white-space: nowrap; }
  .front .title { position: absolute; font-weight: 400; white-space: nowrap; }
  .front .contact { position: absolute; font-weight: 500; white-space: nowrap; }
  .front .contact b { display: inline-block; font-weight: 700; }
  .services {
    position: absolute; left: 0; right: 0; color: var(--paper); font-weight: 400;
    display: flex; align-items: center; justify-content: center; white-space: nowrap;
  }
  .services .sep { margin: 0 0.55em; }
  .address { position: absolute; left: 0; right: 0; text-align: center; font-weight: 500; white-space: nowrap; }
  .brand {
    position: absolute; display: flex; flex-direction: column; align-items: center;
    font-weight: 700; color: var(--ink); white-space: nowrap;
  }
  .brand .dot { border-radius: 50%; border: 2px solid var(--ink); background: var(--paper); }

  /* Back side */
  .back .brand { left: 0; right: 0; }
  .back .name { position: absolute; left: 0; right: 0; text-align: center; font-weight: 500; white-space: nowrap; }
  .badge {
    position: absolute; background: var(--ink); color: var(--paper);
    font-weight: 700; text-align: center; white-space: nowrap;
  }
  .specialty {
    position: absolute; background: var(--paper); border: 1px solid var(--frame); font-weight: 400;
    display: flex; align-items: center; justify-content: center; white-space: nowrap;
  }

  /* Large pink set */
  .front.lg { left: 137px; top: 340px; width: 438px; height: 200px; }
  .front.lg .name { left: 43px; top: 12px; font-size: 14.5px; }
  .front.lg .title { left: 43px; top: 30px; font-size: 11px; }
  .front.lg .contact { left: 43px; top: 51px; font-size: 11px; line-height: 12.5px; }
  .front.lg .contact b { width: 16px; }
  .front.lg .services { top: 124px; height: 29px; background: var(--pink); font-size: 13px; letter-spacing: 0.3px; }
  .front.lg .address { top: 170px; font-size: 11px; }
  .front.lg .brand { left: 285px; top: 22px; width: 80px; font-size: 13px; gap: 6px; }
  .front.lg .brand .dot { width: 34px; height: 34px; }

  .back.lg { left: 625px; top: 291px; width: 437px; height: 250px; background: var(--pink); }
  .back.lg .brand { top: 50px; font-size: 13px; gap: 6px; }
  .back.lg .brand .dot { width: 34px; height: 34px; }
  .back.lg .name { top: 130px; font-size: 19px; letter-spacing: 0.4px; }
  .back.lg .badge { left: 167px; top: 156px; width: 100px; height: 16px; font-size: 8px; line-height: 16px; letter-spacing: 1.4px; }
  .back.lg .specialty { left: 81px; top: 223px; width: 275px; height: 28px; font-size: 9px; letter-spacing: 2px; }

  /* Small lilac set */
  .front.sm { left: 329px; top: 755px; width: 252px; height: 110px; }
  .front.sm .name { left: 24px; top: 6px; font-size: 8.5px; }
  .front.sm .title { left: 24px; top: 16px; font-size: 6px; }
  .front.sm .contact { left: 24px; top: 28px; font-size: 6px; line-height: 7px; }
  .front.sm .contact b { width: 10px; }
  .front.sm .services { top: 71px; height: 16px; background: var(--lilac); font-size: 7px; }
  .front.sm .address { top: 96px; font-size: 6px; font-weight: 700; }
  .front.sm .brand { left: 160px; top: 10px; width: 50px; font-size: 8px; gap: 3px; }
  .front.sm .brand .dot { width: 20px; height: 20px; border-width: 1.5px; }

  .back.sm { left: 619px; top: 726px; width: 252px; height: 144px; background: var(--lilac); }
  .back.sm .brand { top: 30px; font-size: 8px; gap: 3px; }
  .back.sm .brand .dot { width: 20px; height: 20px; border-width: 1.5px; }
  .back.sm .name { top: 74px; font-size: 11px; }
  .back.sm .badge { left: 96px; top: 90px; width: 58px; height: 10px; font-size: 5px; line-height: 10px; letter-spacing: 0.6px; }
  .back.sm .specialty { left: 46px; top: 127px; width: 159px; height: 17px; font-size: 5.5px; letter-spacing: 1px; }
</style>
</head>
<body>

  <!-- Pink set -->
  <section class="card front lg">
    <div class="brand"><span class="dot"></span>Quenby</div>
    <h1 class="name">Marvia Quenby-Fenwick MD</h1>
    <p class="title">Board Certified</p>
    <p class="contact"><b>P:</b>555.210.3318/3319<br><b>F:</b>555.210.3354<br><b>E:</b>q-fenwick@meadowmail.net</p>
    <p class="services">Obstetrics<span class="sep">|</span>Gynecology<span class="sep">|</span>Family Planning<span class="sep">|</span>Menopause</p>
    <p class="address">418 Larkfield Road, Larkfield NY 11040</p>
  </section>

  <section class="card back lg">
    <div class="brand"><span class="dot"></span>Quenby</div>
    <h2 class="name">Marvia Quenby-Fenwick MD</h2>
    <p class="badge">BOARD CERTIFIED</p>
    <p class="specialty">WOMEN'S HEALTH &amp; WELLNESS SPECIALIST</p>
  </section>

  <!-- Lilac set -->
  <section class="card front sm">
    <div class="brand"><span class="dot"></span>Quenby</div>
    <h1 class="name">Marvia Quenby-Fenwick MD</h1>
    <p class="title">Board Certified</p>
    <p class="contact"><b>P:</b>555.210.3318/3319<br><b>F:</b>555.210.3354<br><b>E:</b>q-fenwick@meadowmail.net</p>
    <p class="services">Obstetrics<span class="sep">|</span>Gynecology<span class="sep">|</span>Family Planning<span class="sep">|</span>Menopause</p>
    <p class="address">418 Larkfield Road, Larkfield NY 11040</p>
  </section>

  <section class="card back sm">
    <div class="brand"><span class="dot"></span>Quenby</div>
    <h2 class="name">Marvia Quenby-Fenwick MD</h2>
    <p class="badge">BOARD CERTIFIED</p>
    <p class="specialty">WOMEN'S HEALTH &amp; WELLNESS SPECIALIST</p>
  </section>

</body>
</html>
```